Tranquil Harbour Hypnotherapy 2017 DL Card Flyer

We would like a double sided DL Card Flyer design.

We are a professional Hypnotherapy Clinic looking for a fresh clean design.

Front of card is summary info and back of flyer is detailed text.

I have attached documents with text for the front (dl size hypno 1) and back (dl size hypno 2) of the card and an indicative style of layout.

There are logo files uploaded as well as one image file.

The colors we like are blue, white and yellow/gold.
Updates

please note: when using the 'new mindset new results' image, please only use the top half of the image. The girl is not to be in the image, just the words and light bulb with the chalk underline. thanks.. Added Sunday, March 19, 2017

Industry/Entity Type

Health And Wellness

Requirements
Must have
• Note. I have misspelled the www.TranquilHarbourHypnotherapy.com.au (missing an 'o' in the attachments to the brief). My error. Please amend in your design submissions.

```html
<!DOCTYPE html>
<html lang="en">
<head>
<meta charset="utf-8">
<title>Tranquil Harbour Hypnotherapy – DL Flyer</title>
<link href="https://fonts.googleapis.com/css2?family=Montserrat:wght@700&family=Playball&family=Roboto+Condensed:wght@700&family=Hind:wght@400&display=swap" rel="stylesheet">
<style>
  :root {
    --navy: #1f2b6b;
    --grey: #6b6b6b;
    --grey-dark: #555555;
    --ink: #1c1c1c;
    --white: #ffffff;
    --photo-dark: #2f3033;
    --photo-mid: #4a4b4e;
    --bulb: #f3e27a;
  }
  * { margin: 0; padding: 0; box-sizing: border-box; }
  html, body { width: 1200px; height: 1200px; overflow: hidden; background: var(--white); }
  .canvas { position: relative; width: 1200px; height: 1200px; background: var(--white); }

  .card {
    position: absolute; top: 82px; width: 512px; height: 1052px;
    background: var(--white);
    box-shadow: 3px 4px 8px rgba(0,0,0,0.28);
    overflow: hidden;
  }
  .card--front { left: 74px; }
  .card--back { left: 630px; }

  .brand { position: absolute; display: flex; align-items: center; }
  .brand__dot { width: 112px; height: 112px; border-radius: 50%; background: var(--navy); flex: none; }
  .brand__rule { width: 2px; height: 104px; background: var(--grey); margin: 0 14px 0 12px; }
  .brand__name {
    font-family: "Montserrat", sans-serif; font-weight: 700; color: var(--navy);
    font-size: 21px; line-height: 1.15; letter-spacing: 0.5px; text-transform: uppercase;
  }
  .card--front .brand { left: 92px; top: 38px; }
  .card--back .brand { left: 90px; top: 25px; }

  .quote {
    position: absolute; left: 0; right: 0; top: 178px; z-index: 2; text-align: center;
    font-family: "Playball", cursive; color: var(--navy); font-size: 33px; line-height: 40px;
  }

  .hero { position: absolute; left: 0; top: 236px; width: 512px; height: 400px; z-index: 1; }

  .headline {
    position: absolute; left: 0; right: 0; top: 640px; text-align: center;
    font-family: "Roboto Condensed", sans-serif; font-weight: 700; color: var(--grey-dark);
    font-size: 37px; line-height: 45px;
  }

  .program-list {
    position: absolute; top: 754px; list-style: none;
    font-family: "Hind", sans-serif; font-size: 18px; color: var(--ink); line-height: 21px;
  }
  .program-list li { position: relative; padding-left: 16px; margin-bottom: 8px; }
  .program-list li::before {
    content: ""; position: absolute; left: 0; top: 6px; width: 9px; height: 9px;
    border-radius: 50%; background: var(--navy);
  }
  .program-list--left { left: 44px; }
  .program-list--left li:first-child { line-height: 29px; }
  .program-list--left li:first-child::before { top: 10px; }
  .program-list--right { left: 298px; top: 756px; }
  .program-list--right li { margin-bottom: 10px; }

  .phone-band {
    position: absolute; left: 0; top: 906px; width: 512px; height: 75px; background: var(--navy);
    display: flex; align-items: center; justify-content: center;
    font-family: "Roboto Condensed", sans-serif; font-weight: 700; color: var(--white);
    font-size: 56px; letter-spacing: 1px;
  }

  .web {
    position: absolute; left: 0; right: 0; text-align: center;
    font-family: "Hind", sans-serif; font-size: 16px; color: var(--ink);
  }
  .card--front .web { top: 1010px; }
  .card--back .web { top: 994px; }

  .back-wave { position: absolute; left: 0; top: 100px; width: 512px; height: 120px; }

  .program {
    position: absolute; left: 28px; width: 464px;
    font-family: "Hind", sans-serif; font-size: 17px; line-height: 20.7px; color: var(--ink);
  }
  .program__title {
    font-family: "Roboto Condensed", sans-serif; font-weight: 700; color: var(--navy);
    font-size: 17px; line-height: 21px; text-transform: uppercase;
  }
  .program__body p { text-align: justify; }
  .program--sugar { top: 234px; }
  .program--smoking { top: 376px; }
  .program--fatigue { top: 522px; }
  .program--stress { top: 754px; }

  .footer-band {
    position: absolute; left: 0; top: 886px; width: 512px; height: 92px; background: var(--navy);
    display: flex; align-items: center; justify-content: center; text-align: center;
    font-family: "Roboto Condensed", sans-serif; font-weight: 700; color: var(--white);
    font-size: 16px; line-height: 21px; padding: 0 24px;
  }
</style>
</head>
<body>
<div class="canvas">

  <section class="card card--front">
    <div class="brand">
      <span class="brand__dot"></span>
      <span class="brand__rule"></span>
      <span class="brand__name">Tranquil Harbour<br>Hypnotherapy</span>
    </div>

    <p class="quote">“There is nothing more important<br>than good health”</p>

    <svg class="hero" viewBox="0 0 512 400" xmlns="http://www.w3.org/2000/svg">
      <defs>
        <radialGradient id="hero-glow" cx="0.53" cy="0.45" r="0.55">
          <stop offset="0" stop-color="var(--bulb)"/>
          <stop offset="0.18" stop-color="#8f8a5c"/>
          <stop offset="0.5" stop-color="var(--photo-mid)"/>
          <stop offset="1" stop-color="var(--photo-dark)"/>
        </radialGradient>
      </defs>
      <path d="M0 88 C150 100 330 48 512 28 L512 332 C330 322 170 372 0 357 Z"
            fill="url(#hero-glow)" role="img"
            aria-label="Chalkboard with a glowing light bulb and the words New Mindset, New Results"/>
      <path d="M0 54 C150 70 330 20 512 0 L512 14 C330 36 150 86 0 76 Z" fill="var(--navy)"/>
      <path d="M0 76 C150 86 330 36 512 14 L512 30 C330 50 150 100 0 90 Z" fill="var(--grey)"/>
      <path d="M0 355 C170 370 330 320 512 330 L512 344 C330 334 170 384 0 372 Z" fill="var(--grey)"/>
      <path d="M0 376 C170 390 330 338 512 348 L512 360 C330 352 170 404 0 396 Z" fill="var(--navy)"/>
    </svg>

    <h1 class="headline">Professional Hypnosis<br>Therapy Programs:</h1>

    <ul class="program-list program-list--left">
      <li>Weight Loss<br>(Virtual Gastric Band)</li>
      <li>Sugar Addiction</li>
      <li>Quit Smoking</li>
    </ul>
    <ul class="program-list program-list--right">
      <li>Chronic Fatigue &amp;<br>Chronic Pain Relief</li>
      <li>Stress Relief &amp;<br>Deep Relaxation</li>
    </ul>

    <div class="phone-band">1300 555 019</div>
    <p class="web">www.TranquilHarbourHypnotherapy.com.au</p>
  </section>

  <section class="card card--back">
    <div class="brand">
      <span class="brand__dot"></span>
      <span class="brand__rule"></span>
      <span class="brand__name">Tranquil Harbour<br>Hypnotherapy</span>
    </div>

    <svg class="back-wave" viewBox="0 0 512 120" xmlns="http://www.w3.org/2000/svg">
      <path d="M0 58 C160 80 330 60 512 8 L512 38 C330 82 170 120 0 102 Z" fill="var(--navy)"/>
      <path d="M250 100 C340 88 420 66 512 44 L512 64 C420 80 340 96 250 100 Z" fill="var(--grey)"/>
    </svg>

    <article class="program program--sugar">
      <h2 class="program__title">Sugar Addiction Program</h2>
      <div class="program__body">
        <p>Excess sugar intake can lead to obesity, Type 2 Diabetes and tooth decay.The habit of reaching for soft drinks, chocolate, sweets, cakes and biscuits can be hard to break.By rewiring your subconscious habits, our Program puts you back in control.Number of Sessions: 3+</p>
      </div>
    </article>

    <article class="program program--smoking">
      <h2 class="program__title">Quit Smoking Program</h2>
      <div class="program__body">
        <p>The facts speak for themselves. You are 10 times more likely to quit smoking for good using hypnotherapy.</p>
        <p>Expect to be a non smoker after completing the first session of our Program. (12 Month Guarantee)</p>
        <p>Number of Sessions: 2</p>
      </div>
    </article>

    <article class="program program--fatigue">
      <h2 class="program__title">Chronic Fatigue &amp; Chronic Pain Relief Program</h2>
      <div class="program__body">
        <p>Chronic Fatigue, Fibromyalgia and Chronic Musculoskeletal Pain are diseases of modern living.</p>
        <p>The symptoms of fatigue and pain are very real, however the cause is usually emotional, and is generally hidden beyond our conscious awareness.</p>
        <p>Our Program comprises Education and Hypnosis to help you regain your health, your self esteem, your friends and your life, all in a manageable timeframe.</p>
        <p>Number of Sessions: 6</p>
      </div>
    </article>

    <article class="program program--stress">
      <h2 class="program__title">Stress Relief &amp; Deep Relaxation Program</h2>
      <div class="program__body">
        <p>Our Program gently uncovers the true source of your stress, and helps you reconnect to a natural inner calm. We teach you self hypnosis so that you have the tools to continue your experience.Number of Sessions: 3+</p>
      </div>
    </article>

    <div class="footer-band">All Programs include take home CD’s personally recorded by our therapists, using advanced hypnotic techniques.</div>
    <p class="web">www.TranquilHarbourHypnotherapy.com.au</p>
  </section>

</div>
</body>
</html>
```